Kelvane Plumbing Business cards

Company is Kelvane Plumbing.
name Dashel Morrowby, I am a plumber, drainer, gasfitter and roofer
Mobile: 0431 906 154
Email address: info@kelvaneplumbing.example (check out my website for some ideas)
Website: www.kelvaneplumbing.example
ABN: 82 916 203 471
LIC: 604517K

I am reliable all round plumber. I am a 24 hour emergency service. Kelvane Plumbing is a professional plumbing service in the Illawarra, South Coast, Southern Sydney and Southern Highland regions of NSW. We offer a 24 hour emergency service for piece of mind to our customers. Call us now to see how we can help you. Kelvane Plumbing approaches every job with attention to detail and excellent customer service. With our superior workmanship you can be confident that the job will be done right the first time around. You can rest assured with results that are guaranteed to last.

Target Market(s)

the general public

Contact Information for Business Card

look up website for some ideas something with similar colours to logo and new modern and to catch the eye.

Colors
fdfdfd
ffffff
000000
7f7f7f
aaaaaa
33a6d7
0492cd

Requirements
Must have
• all contact details
• company- Kelvane Plumbing
• name- Dashel Morrowby
• number mobile- 0431 906 154
• Email address- info@kelvaneplumbing.example
• Website- www.kelvaneplumbing.example
• ABN- 82 916 203 471
• LIC- 604517K

```html
<!DOCTYPE html>
<html lang="en">
<head>
<meta charset="utf-8">
<title>Kelvane Plumbing – Business Cards</title>
<link rel="stylesheet" href="https://fonts.googleapis.com/css2?family=Poppins:wght@600&family=Questrial&display=swap">
<style>
  :root {
    --canvas-bg: #e6e8eb;
    --card-dark: #121620;
    --card-light: #ffffff;
    --brand-blue: #0492cd;
    --brand-blue-soft: #33a6d7;
    --brand-grey: #7f7f7f;
    --brand-grey-light: #aaaaaa;
    --text-dark: #000000;
  }
  * { margin: 0; padding: 0; box-sizing: border-box; }
  html, body { width: 1200px; height: 880px; overflow: hidden; }
  body {
    background: var(--canvas-bg);
    font-family: "Questrial", "Century Gothic", sans-serif;
    position: relative;
  }
  .card {
    position: absolute;
    left: 280px;
    width: 640px;
    height: 366px;
    border-radius: 22px;
    box-shadow: 0 12px 30px rgba(0,0,0,0.18);
    overflow: hidden;
  }
  .card--back { top: 60px; background: var(--card-dark); }
  .card--front { top: 456px; background: var(--card-light); }

  /* back card brand */
  .brand-lockup {
    position: absolute;
    inset: 0;
    display: flex;
    align-items: center;
    justify-content: center;
    gap: 16px;
  }
  .brand-lockup__dot {
    width: 22px; height: 22px;
    border-radius: 50%;
    background: var(--brand-blue-soft);
  }
  .brand-lockup__name {
    font-family: "Poppins", "Century Gothic", sans-serif;
    font-weight: 600;
    font-size: 30px;
    color: var(--brand-blue-soft);
    letter-spacing: 0.5px;
  }

  /* front card */
  .front__decor {
    position: absolute;
    right: 40px;
    top: 44px;
    width: 200px;
    height: 200px;
    border-radius: 50%;
    background: var(--brand-blue);
    opacity: 0.9;
  }
  .front__info {
    position: absolute;
    left: 44px;
    top: 92px;
    width: 340px;
  }
  .company-name {
    font-family: "Poppins", "Century Gothic", sans-serif;
    font-weight: 600;
    font-size: 30px;
    color: var(--brand-blue);
    line-height: 1.1;
    margin-bottom: 20px;
    white-space: nowrap;
  }
  .person-name {
    font-family: "Poppins", "Century Gothic", sans-serif;
    font-weight: 600;
    font-size: 20px;
    color: var(--brand-blue);
    line-height: 1.15;
  }
  .person-role {
    font-size: 14px;
    color: var(--brand-grey);
    margin-bottom: 16px;
  }
  .contact-list { list-style: none; }
  .contact-list__item {
    display: flex;
    align-items: center;
    gap: 10px;
    font-size: 14px;
    color: var(--brand-grey);
    line-height: 1;
    margin-bottom: 7px;
  }
  .contact-list__icon {
    width: 18px; height: 18px;
    border-radius: 50%;
    background: var(--brand-blue-soft);
    display: flex; align-items: center; justify-content: center;
    flex-shrink: 0;
  }
  .contact-list__accent { color: var(--brand-blue); }
  .registration {
    font-size: 14px;
    color: var(--brand-grey);
    margin-top: 10px;
  }
</style>
</head>
<body>

<section class="card card--back" aria-label="Business card back">
  <div class="brand-lockup">
    <span class="brand-lockup__dot"></span>
    <span class="brand-lockup__name">Kelvane Plumbing</span>
  </div>
</section>

<section class="card card--front" aria-label="Business card front">
  <div class="front__decor" role="img" aria-label="Large brand decoration area in brand blue"></div>

  <div class="front__info">
    <h1 class="company-name">Kelvane Plumbing</h1>
    <p class="person-name">Dashel Morrowby</p>
    <p class="person-role">Plumber | Drainer |Gasfitter | Roofer</p>

    <ul class="contact-list">
      <li class="contact-list__item">
        <span class="contact-list__icon">
          <svg width="10" height="10" viewBox="0 0 10 10"><rect x="2.5" y="0.5" width="5" height="9" rx="1" fill="none" stroke="#fff" stroke-width="1.2"/></svg>
        </span>
        0431 906 154
      </li>
      <li class="contact-list__item">
        <span class="contact-list__icon">
          <svg width="10" height="10" viewBox="0 0 10 10"><rect x="0.8" y="2" width="8.4" height="6" fill="none" stroke="#fff" stroke-width="1.1"/><path d="M1 2.3 L5 5.5 L9 2.3" fill="none" stroke="#fff" stroke-width="1.1"/></svg>
        </span>
        info@kelvaneplumbing.example
      </li>
      <li class="contact-list__item">
        <span class="contact-list__icon">
          <svg width="10" height="10" viewBox="0 0 10 10"><circle cx="5" cy="5" r="4" fill="none" stroke="#fff" stroke-width="1.1"/><path d="M1 5 H9 M5 1 V9" stroke="#fff" stroke-width="0.9"/></svg>
        </span>
        <span>www.<span class="contact-list__accent">kelvaneplumbing</span>.example</span>
      </li>
    </ul>

    <p class="registration">ABN- 82 916 203 471 | LIC- 604517K</p>
  </div>
</section>

</body>
</html>
```